KORBALT

The business want a professional looking business card. We have a scetch we will add but want the extra upgrade, and would like more suggestions for variations of our business cards.

```html
<!DOCTYPE html>
<html lang="en">
<head>
<meta charset="utf-8">
<title>KORBALT Business Card</title>
<link href="https://fonts.googleapis.com/css2?family=Montserrat:wght@400;500;600;700&display=swap" rel="stylesheet">
<style>
  :root {
    --page-bg: #ffffff;
    --label: #777777;
    --gold-light: #d3bd7f;
    --gold-mid: #b89a5a;
    --gold-dark: #7c5a28;
    --gold-pale: #f8efbd;
    --ink-brown: #6a4a1c;
    --ink-white: #ffffff;
    --band-top: #d6c69a;
    --band-bottom: #a88a4f;
  }
  * { margin: 0; padding: 0; box-sizing: border-box; }
  html, body {
    width: 1200px; height: 679px; overflow: hidden;
    background: var(--page-bg);
    font-family: "Montserrat", sans-serif;
  }
  .sheet { position: relative; width: 1200px; height: 679px; }
  .side-label {
    position: absolute; top: 147px; width: 200px; margin-left: -100px;
    text-align: center; font-size: 18px; font-weight: 400;
    letter-spacing: 0.5px; color: var(--label);
  }
  .card {
    position: absolute; top: 209px; width: 422px; height: 252px; overflow: hidden;
    background:
      radial-gradient(ellipse 55% 70% at 92% 95%, var(--gold-pale) 0%, rgba(248,239,189,0) 100%),
      radial-gradient(ellipse 45% 55% at 100% 0%, var(--gold-dark) 0%, rgba(124,90,40,0) 100%),
      radial-gradient(ellipse 40% 60% at 0% 100%, var(--gold-dark) 0%, rgba(124,90,40,0) 100%),
      linear-gradient(120deg, var(--gold-light) 0%, var(--gold-mid) 55%, #e6d595 100%);
    box-shadow: 0 18px 34px rgba(120, 95, 50, 0.28);
  }
  .card--front { left: 125px; }
  .card--back { left: 656px; }

  .wordmark {
    position: absolute; left: 0; right: 0; text-align: center;
    font-weight: 600; color: var(--ink-brown);
  }
  .wordmark__name { letter-spacing: 2px; line-height: 1; }
  .wordmark__since { font-size: 12px; letter-spacing: 3px; margin-top: 8px; font-weight: 500; }
  .card--front .wordmark { top: 104px; }
  .card--front .wordmark__name { font-size: 34px; }

  .card--back .wordmark { left: 190px; right: 12px; top: 126px; }
  .card--back .wordmark__name { font-size: 26px; }
  .card--back .wordmark__since { font-size: 10px; margin-top: 6px; }

  .holder { position: absolute; left: 39px; top: 51px; color: var(--ink-brown); }
  .holder__company { font-size: 15px; font-weight: 700; letter-spacing: 0.4px; }
  .holder__role { font-size: 10.5px; font-weight: 500; margin-top: 6px; line-height: 1.2; }
  .holder__person { font-size: 10.5px; font-weight: 500; line-height: 1.2; }

  .contacts { position: absolute; left: 39px; top: 124px; list-style: none; }
  .contacts__item {
    display: flex; align-items: center; height: 16px; margin-bottom: 9px;
    font-size: 11.5px; font-weight: 500; color: var(--ink-white);
  }
  .contacts__icon { width: 14px; height: 14px; margin-right: 17px; flex: none; }

  .card__band {
    position: absolute; left: 0; right: 0; bottom: 0; height: 37px;
    background: linear-gradient(180deg, var(--band-top) 0%, #c8b27c 40%, var(--band-bottom) 100%);
  }
</style>
</head>
<body>
<main class="sheet">
  <div class="side-label" style="left:333px">FRONT</div>
  <div class="side-label" style="left:867px">BACK</div>

  <section class="card card--front" aria-label="Card front">
    <div class="wordmark">
      <div class="wordmark__name">KORBALT</div>
      <div class="wordmark__since">SINCE 2026</div>
    </div>
  </section>

  <section class="card card--back" aria-label="Card back">
    <div class="holder">
      <div class="holder__company">KORBALT SOLVANG</div>
      <div class="holder__role">CEO &amp; FOUNDER</div>
      <div class="holder__person">Lars Henrik Solvang</div>
    </div>

    <ul class="contacts">
      <li class="contacts__item">
        <svg class="contacts__icon" viewBox="0 0 14 14" fill="none" stroke="#fff" stroke-width="1.2">
          <circle cx="7" cy="7" r="6"/><ellipse cx="7" cy="7" rx="2.6" ry="6"/>
          <line x1="1" y1="7" x2="13" y2="7"/>
        </svg>
        www.korbalt.llc
      </li>
      <li class="contacts__item">
        <svg class="contacts__icon" viewBox="0 0 14 14" fill="#fff">
          <path d="M3 1.2l2 .1 1.2 3-1.4 1.1c.7 1.5 1.8 2.6 3.3 3.3l1.1-1.4 3 1.2.1 2c-.2.9-1 1.5-1.9 1.4C5.6 11.6 2.4 8.4 1.6 3.1 1.5 2.2 2.1 1.4 3 1.2z"/>
        </svg>
        004791234567
      </li>
      <li class="contacts__item">
        <svg class="contacts__icon" viewBox="0 0 14 14">
          <rect x="1" y="3" width="12" height="8.5" rx="1" fill="#fff"/>
          <path d="M1.6 3.6L7 7.8l5.4-4.2" fill="none" stroke="#b89a5a" stroke-width="1.1"/>
        </svg>
        korbalt.llc@mailbox.com
      </li>
    </ul>

    <div class="wordmark">
      <div class="wordmark__name">KORBALT</div>
      <div class="wordmark__since">SINCE 2026</div>
    </div>

    <div class="card__band"></div>
  </section>
</main>
</body>
</html>
```